Biz Card Design TPVC

New business card for a new company.
Logo was completed by a designer on ArtFlock and looking to continue requesting additional services.
Company Name: Tidal Prime Voltage Collective
Although this company is starting in Canada, we will be moving towards a global presence within the next 6 months.
Key elements to this business are as follows.
Energy Procurement
Energy Reduction Services
Demand Side Consulting
Energy Efficiency Consulting
Saving Clients Money
Helping Them Go "Green"
Managing Their Energy Requirements
Basically the goal for our company is to find the best procurement solution for our clients and reduce their energy consumption. This reduces their expenses and the amount of greenhouse gas they produce on a daily basis.
I have been in the energy footprint for the last 20 years and know that most companies are looking to "do whatever is necessary to get them to sign on the dotted line". I would prefer to walk away from a client that I can't help than to put them into a situation that they will regret for years to come. This is where the "TIDAL" part of the company name comes from.
The following is a catch phrase that encompasses what we do.
"Reducing your carbon footprint & energy bill at the same time!"
The back of the card needs to have this statement along with some sort of illustration. The back is a playground for creative ideas.
The front of the card needs the following.
Logo.
First & Last Name (Gus Marwick)
Title (Energy Warrior)
Phone Number (555) 314-2768
Fax Number (555) 862-4091
Email Address gus@tidalprimevoltage.example
Address 47 Orchard Lane Toronto Ontario K4P 2Z7
I want it to be a card that is remembered when any of my staff give it to a customer. It HAS to stand out.
Target Market(s)
Business Owners, Decision Makers, 30 to 65+
Industry/Entity Type
Business
Look and feel
Each slider illustrates characteristics of the customer's brand and the style your logo design should communicate.

```html
<!DOCTYPE html>
<html lang="en">
<head>
<meta charset="utf-8">
<title>Tidal Prime Voltage Collective — Business Card</title>
<link rel="stylesheet" href="https://fonts.googleapis.com/css2?family=Open+Sans:wght@400;600&family=Oxygen:wght@400&display=swap">
<style>
  :root {
    --backdrop: #8f8f8f;
    --card-white: #ffffff;
    --leaf-green: #3fa62f;
    --leaf-green-light: #8fd27a;
    --text-green: #3aa52a;
    --band-blue: #3b57b3;
    --title-blue: #3b57b3;
    --back-green: #42ad2f;
    --back-glow: #9ad98a;
    --tagline: #ffffff;
  }
  * { box-sizing: border-box; margin: 0; padding: 0; }
  html, body {
    width: 1200px; height: 969px; overflow: hidden;
    background: var(--backdrop);
    font-family: "Open Sans", sans-serif;
  }
  .sheet {
    width: 1200px; height: 969px;
    display: flex; flex-direction: column; align-items: center; justify-content: center;
    gap: 50px;
  }
  .card {
    position: relative; width: 700px; height: 400px; overflow: hidden;
    box-shadow: 0 6px 18px rgba(0,0,0,.25);
  }
  /* Front */
  .card-front { background: var(--card-white); }
  .mark-circle {
    position: absolute; left: 70px; top: 60px; width: 170px; height: 170px;
    border-radius: 50%; background: var(--leaf-green);
  }
  .name-band {
    position: absolute; left: 180px; right: 0; top: 160px; height: 40px;
    background: var(--band-blue);
    display: flex; align-items: center; padding-left: 90px;
  }
  .band-name {
    color: #fff; font-weight: 600; font-size: 19px; letter-spacing: .2px;
  }
  .person { position: absolute; right: 40px; top: 72px; text-align: right; }
  .person-name {
    font-family: "Oxygen", sans-serif; color: var(--text-green);
    font-size: 34px; letter-spacing: 1px;
  }
  .person-title {
    font-family: "Oxygen", sans-serif; color: var(--title-blue);
    font-size: 17px; letter-spacing: .5px; margin-top: 2px;
  }
  .contact {
    position: absolute; left: 400px; top: 250px; color: var(--text-green);
    font-size: 13px; line-height: 1.35;
  }
  .contact-row { display: flex; gap: 12px; align-items: flex-start; margin-bottom: 10px; }
  .contact-icon { width: 16px; height: 16px; flex: none; margin-top: 2px; }
  .contact-small { font-size: 11px; }
  /* Back */
  .card-back {
    background: radial-gradient(ellipse 55% 60% at 50% 42%, var(--back-glow) 0%, var(--back-green) 70%);
  }
  .back-mark {
    position: absolute; left: 50%; top: 70px; width: 80px; height: 80px; margin-left: -40px;
    border-radius: 50%; background: rgba(255,255,255,.35);
  }
  .back-name {
    position: absolute; left: 0; right: 0; top: 168px; text-align: center;
    color: #c6ec4a; font-weight: 600; font-size: 34px;
  }
  .tagline {
    position: absolute; left: 0; right: 0; top: 262px; text-align: center;
    color: var(--tagline); font-size: 21px;
  }
</style>
</head>
<body>
<main class="sheet">
  <section class="card card-front" aria-label="Card front">
    <div class="mark-circle"></div>
    <div class="name-band"><span class="band-name">Tidal Prime Voltage Collective</span></div>
    <div class="person">
      <p class="person-name">Gus Marwick</p>
      <p class="person-title">Energy Warrior</p>
    </div>
    <div class="contact">
      <div class="contact-row">
        <svg class="contact-icon" viewBox="0 0 24 24" aria-hidden="true"><path fill="#3b57b3" d="M6.6 10.8a15.2 15.2 0 0 0 6.6 6.6l2.2-2.2a1 1 0 0 1 1-.25 11.4 11.4 0 0 0 3.6.57 1 1 0 0 1 1 1V20a1 1 0 0 1-1 1A17 17 0 0 1 3 4a1 1 0 0 1 1-1h3.5a1 1 0 0 1 1 1c0 1.25.2 2.45.57 3.57a1 1 0 0 1-.25 1z"/></svg>
        <div><p>(555) 314-2768</p><p>(555) 862-4091</p></div>
      </div>
      <div class="contact-row">
        <svg class="contact-icon" viewBox="0 0 24 24" aria-hidden="true"><rect x="2" y="5" width="20" height="14" rx="1" fill="#3b57b3"/><path d="M3 6l9 7 9-7" stroke="#fff" stroke-width="1.6" fill="none"/></svg>
        <div class="contact-small"><p>gus@tidalprimevoltage.example</p><p>47 Orchard Lane Toronto Ontario K4P 2Z7</p></div>
      </div>
    </div>
  </section>
  <section class="card card-back" aria-label="Card back">
    <div class="back-mark"></div>
    <p class="back-name">Tidal Prime Voltage Collective</p>
    <p class="tagline">Reducing your carbon footprint &amp; energy bill at the same time !</p>
  </section>
</main>
</body>
</html>
```